Tidal Hounds Dog Behaviour, Training and Natural Healthcare Business Card Design

I am an experienced and qualified dog behavioural trainer and natural animal healthcare consultant offering a range of services to help pet dog owners with the "whole dog".
COLOURS: A soft light blue in the background - can be fading out or split, red should also feature
LOGO: Dog, healing hands, silhouette, shadow
SERVICES: Behaviour Consults, Training, Complex Skills Coaching Walking Coaching, Diet & Nutrition, Environmental Enrichment, Lifestyle and Lifestage Adaptations, Massage, Natural Health Options
BY LINE: Happy Dogs, Happy Owners
VALUES: Promoting communication and connection between dogs and their owners.
FOCUS: Nutritional guidance and environmental adaptation are often needed to complete the package and increase the success rate of training and behaviour modification.

Target Market(s)

Everyone who has a dog who they wish to improve their relationship with

Industry/Entity Type

Communication

Contact Information for Business Card

Tidal Hounds, Rosalind Vukovic, 0417 286350, tidalhounds7@quellmail.net, www.tidalhounds7.net, Qualified Dog Behavioural Trainer and Natural Animal Healthcare Consultant

Font styles to use
Sans Serif
Script

Colors
85cae6
ec2027

Requirements
Must have
• A clear indication that it is a dog services business. A raised feature
Should not have
• Pawprints, cartoons

Files

```html
<!DOCTYPE html>
<html lang="en">
<head>
<meta charset="utf-8">
<title>Tidal Hounds Business Card</title>
<link rel="stylesheet" href="https://fonts.googleapis.com/css2?family=Arimo:wght@400&family=Noto+Sans:wght@400;700&display=swap">
<style>
  :root {
    --stage: #1a1a1a;
    --card-white: #ffffff;
    --sky: #85cae6;
    --sky-deep: #1aa3e0;
    --brand-blue: #1a9fdf;
    --ink: #000000;
  }
  html, body {
    margin: 0;
    width: 1200px;
    height: 1000px;
    overflow: hidden;
    background: var(--stage);
  }
  .business-card {
    position: absolute;
    left: 290px;
    top: 313px;
    width: 620px;
    height: 373px;
    background: var(--card-white);
    overflow: hidden;
  }
  .card-backdrop {
    position: absolute;
    inset: 0;
  }
  .brand-name {
    position: absolute;
    left: 46px;
    top: 8px;
    margin: 0;
    font-family: "Noto Sans", sans-serif;
    font-weight: 400;
    font-size: 70px;
    line-height: 1;
    color: var(--brand-blue);
    white-space: nowrap;
  }
  .tagline {
    position: absolute;
    left: 50px;
    top: 108px;
    margin: 0;
    font-family: "Noto Sans", sans-serif;
    font-weight: 700;
    font-size: 23px;
    line-height: 1.2;
    color: var(--ink);
    white-space: nowrap;
  }
  .tagline-accent { color: var(--brand-blue); }
  .tagline-rule {
    position: absolute;
    left: 48px;
    top: 143px;
    width: 524px;
    height: 3px;
    background: var(--ink);
  }
  .credentials {
    position: absolute;
    left: 46px;
    top: 151px;
    margin: 0;
    font-family: "Arimo", sans-serif;
    font-size: 14px;
    color: var(--ink);
    white-space: nowrap;
  }
  .dog-figure {
    position: absolute;
    left: 22px;
    top: 204px;
    width: 133px;
    height: 152px;
    border-radius: 40px 40px 12px 12px;
    background: linear-gradient(160deg, #222 0%, #000 100%);
  }
  .contact-block {
    position: absolute;
    right: 40px;
    top: 234px;
    text-align: right;
    font-family: "Arimo", sans-serif;
    color: var(--ink);
  }
  .contact-name {
    margin: 0 0 17px;
    font-size: 23px;
    font-weight: 400;
    line-height: 1.2;
  }
  .contact-line {
    margin: 0;
    font-size: 17px;
    line-height: 23px;
  }
  .contact-line.web { margin-top: 3px; }
</style>
</head>
<body>
  <div class="business-card">
    <svg class="card-backdrop" width="620" height="373" viewBox="0 0 620 373" aria-hidden="true">
      <defs>
        <linearGradient id="sky-fade" x1="0.22" y1="0.7" x2="1" y2="0.1">
          <stop offset="0.28" stop-color="#ffffff"/>
          <stop offset="0.55" stop-color="#a8dcf3"/>
          <stop offset="1" stop-color="#1aa3e0"/>
        </linearGradient>
        <linearGradient id="swoosh-glow" x1="0" y1="0" x2="1" y2="1">
          <stop offset="0" stop-color="#ffffff" stop-opacity="0.9"/>
          <stop offset="1" stop-color="#ffffff" stop-opacity="0"/>
        </linearGradient>
      </defs>
      <rect width="620" height="373" fill="url(#sky-fade)"/>
      <path d="M330 40 C420 5 560 0 605 30 C560 70 530 160 530 215 C560 150 600 90 610 40 C600 20 560 12 520 12 C450 12 380 25 330 40 Z" fill="url(#swoosh-glow)"/>
    </svg>

    <h1 class="brand-name">Tidal Hounds</h1>
    <p class="tagline"><span class="tagline-accent">“happy owners"</span> to "Happy Owners"</p>
    <div class="tagline-rule"></div>
    <p class="credentials">Qualified Dog Behavioural Trainer and Natural Animal Healthcare Consultant</p>

    <div class="dog-figure" role="img" aria-label="Black silhouette of a seated puppy looking upward"></div>

    <address class="contact-block">
      <p class="contact-name">Rosalind Vukovic</p>
      <p class="contact-line">0417 286350</p>
      <p class="contact-line">tidalhounds7@quellmail.net</p>
      <p class="contact-line web">www.tidalhounds7.net</p>
    </address>
  </div>
</body>
</html>
```